lantern institute of business and technology web site

I need web site for the institute which focus on business courses and computer course it is also for vocation train for employment It is also carear development and advancement .It should have links to online study resource which free
Industry/Entity Type
Business
Number of Pages Required
1 page
Look and feel

```html
<!DOCTYPE html>
<html lang="en">
<head>
<meta charset="utf-8">
<title>Lantern Institute of Business and Technology</title>
<link href="https://fonts.googleapis.com/css2?family=Open+Sans:wght@400;600;700&family=Roboto:wght@300;400;500;700&display=swap" rel="stylesheet">
<style>
:root{
  --blue:#1e9fe0;
  --blue-dark:#1578b8;
  --navy:#1d3f72;
  --ink:#3a3a3a;
  --muted:#8a8a8a;
  --line:#e6e6e6;
  --footer:#2c2d2f;
  --footer-dark:#262729;
  --white:#ffffff;
}
*{margin:0;padding:0;box-sizing:border-box}
html,body{width:673px;height:1200px;overflow:hidden;background:var(--white)}
body{font-family:"Open Sans",Arial,sans-serif;color:var(--ink);font-size:6px;line-height:1.5}
.page{position:relative;width:673px;height:1200px;overflow:hidden}

/* header */
.site-header{height:62px;display:flex;align-items:center;padding:0 40px 0 34px;background:var(--white)}
.brand{display:flex;align-items:center;gap:6px;font-family:"Roboto",sans-serif;font-weight:700;font-size:9px;color:var(--navy);text-transform:uppercase;letter-spacing:.3px}
.brand-mark{width:22px;height:22px;background:var(--navy)}
.main-nav{margin-left:auto;display:flex;align-items:center;gap:30px;font-family:"Roboto",sans-serif;font-size:6.5px;font-weight:500;color:var(--ink);text-transform:uppercase}
.btn{display:inline-block;background:var(--blue);color:var(--white);font-family:"Roboto",sans-serif;font-size:6px;font-weight:500;text-transform:uppercase;padding:6px 12px;letter-spacing:.3px}
.main-nav .btn{margin-left:4px}

/* hero */
.hero{position:relative;height:274px}
.hero-photo{position:absolute;inset:0;background:linear-gradient(90deg,#e9edf1 0%,#dfe5ea 40%,#cfd8de 62%,#d9e1e6 80%,#c7d0d6 100%)}
.hero-card{position:absolute;left:46px;top:44px;width:238px;background:rgba(255,255,255,.85);padding:10px 12px}
.hero-card h1{font-family:"Roboto",sans-serif;font-size:17px;font-weight:500;color:var(--blue);line-height:1.2;margin-bottom:4px}
.hero-card p{font-size:7px;color:var(--ink);line-height:1.45}
.hero-arrow{position:absolute;top:128px;width:14px;height:18px;background:rgba(60,60,60,.55);display:flex;align-items:center;justify-content:center}
.hero-arrow.prev{left:10px}
.hero-arrow.next{right:10px}

/* search */
.course-search{height:48px;background:var(--blue);display:flex;align-items:center;gap:10px;padding:0 40px 0 46px}
.course-search label{font-family:"Roboto",sans-serif;font-weight:700;font-size:6.5px;color:var(--white);text-transform:uppercase;margin-right:4px}
.field{width:86px;height:16px;background:var(--white);font-size:5.5px;color:var(--muted);padding:0 5px;display:flex;align-items:center;justify-content:space-between}
.field.wide{width:100px}
.course-search .btn{background:var(--navy);margin-left:auto}

/* welcome */
.welcome{display:flex;padding:30px 46px 0 50px;gap:40px;height:220px}
.welcome-intro{width:270px}
.section-label{font-family:"Roboto",sans-serif;font-size:9px;font-weight:500;text-transform:uppercase;color:var(--ink);margin-bottom:6px}
.lead{color:var(--blue);font-size:7px;margin-bottom:6px}
.body-text{font-size:5.8px;color:var(--muted);margin-bottom:6px}
.course-teasers{flex:1;display:flex;flex-direction:column;gap:18px}
.teaser{display:flex;gap:8px}
.teaser-icon{width:14px;flex:none}
.teaser h3{font-family:"Roboto",sans-serif;font-size:7.5px;font-weight:500;color:var(--blue-dark);margin-bottom:3px}
.read-more{font-size:5.8px;color:var(--blue-dark);font-weight:600}

/* business */
.business{display:flex;margin:0 50px;height:152px}
.business-intro{width:128px;background:var(--blue);color:var(--white);padding:16px 12px}
.business-intro h2{font-family:"Roboto",sans-serif;font-size:17px;font-weight:500;line-height:1.1}
.business-intro h2 span{display:block;font-weight:300;font-size:12px}
.business-intro p{font-size:5.6px;opacity:.9;margin:8px 0 12px}
.btn.ghost{background:transparent;border:1px solid var(--white)}
.course-card{position:relative;flex:1}
.course-card .photo{position:absolute;inset:0}
.course-card:nth-child(2) .photo{background:linear-gradient(160deg,#c9b9a6,#8f7866)}
.course-card:nth-child(3) .photo{background:linear-gradient(160deg,#d8c3b0,#9c7f68)}
.course-card:nth-child(4) .photo{background:linear-gradient(160deg,#8b6f56,#3f3b3a)}
.course-card .caption{position:absolute;left:0;right:0;bottom:0;height:16px;background:rgba(30,30,30,.75);color:var(--white);font-size:6px;display:flex;align-items:center;justify-content:space-between;padding:0 8px}

/* computer */
.computer{padding:30px 50px 0;height:320px}
.computer h2{text-align:center;font-family:"Roboto",sans-serif;font-size:17px;font-weight:400;color:var(--blue-dark)}
.computer .subtitle{text-align:center;font-size:6px;color:var(--muted);margin:2px 0 18px}
.computer-body{display:flex;gap:46px}
.monitor{width:210px;height:180px;flex:none;margin-left:10px;background:linear-gradient(180deg,#2a6fc0,#1b4f91 70%,#cfd3d7 72%,#e9ebed)}
.features{flex:1;padding-top:4px}
.feature{display:flex;gap:10px;margin-bottom:12px}
.feature-icon{width:18px;height:18px;border-radius:50%;border:1px solid var(--blue);flex:none;display:flex;align-items:center;justify-content:center}
.feature h3{font-size:6.3px;font-weight:600;color:var(--blue-dark);margin-bottom:2px}
.feature p{font-size:5.6px;color:var(--muted)}
.features .btn{margin-left:28px}

/* footer */
.site-footer{position:absolute;left:0;right:0;bottom:0;height:112px;background:var(--footer);color:#c9c9c9}
.contact-row{display:flex;justify-content:space-between;padding:22px 50px 0;font-size:5.8px}
.contact-row div{display:flex;align-items:center;gap:5px}
.social-row{display:flex;justify-content:center;gap:6px;margin-top:16px}
.social-row span{width:14px;height:14px;border-radius:50%;border:1px solid #6c6c6c}
.copyright{position:absolute;left:0;right:0;bottom:0;height:28px;background:var(--footer-dark);font-size:5.4px;text-align:center;line-height:28px;color:#8f8f8f;text-transform:uppercase}
</style>
</head>
<body>
<div class="page">

<header class="site-header">
  <div class="brand"><span class="brand-mark"></span>Lantern Institute</div>
  <nav class="main-nav">
    <span>Home</span><span>About</span><span>Courses</span><span>Blog</span><span>Contacts</span>
    <span class="btn">Book Your Course</span>
  </nav>
</header>

<section class="hero">
  <div class="hero-photo" role="img" aria-label="Student reading and taking notes at a library desk, bookshelves behind"></div>
  <div class="hero-card">
    <h1>Starts Your Courses Today</h1>
    <p>Learn practical skills that move your career forward, with flexible classes, trusted tutors and free online study help.</p>
  </div>
  <span class="hero-arrow prev"><svg width="6" height="8" viewBox="0 0 6 8"><path d="M5 0L1 4l4 4" fill="none" stroke="#fff" stroke-width="1.4"/></svg></span>
  <span class="hero-arrow next"><svg width="6" height="8" viewBox="0 0 6 8"><path d="M1 0l4 4-4 4" fill="none" stroke="#fff" stroke-width="1.4"/></svg></span>
</section>

<section class="course-search">
  <label>Find your course:</label>
  <span class="field wide">Course Keyword</span>
  <span class="field">Business Courses <svg width="5" height="3"><path d="M0 0h5L2.5 3z" fill="#999"/></svg></span>
  <span class="field">Computer Courses <svg width="5" height="3"><path d="M0 0h5L2.5 3z" fill="#999"/></svg></span>
  <span class="btn">Find a Course</span>
</section>

<section class="welcome">
  <div class="welcome-intro">
    <h2 class="section-label">Welcome to Lantern Institute</h2>
    <p class="lead">Career training built around the needs of employers, helping every learner grow with confidence.</p>
    <p class="body-text">Our programmes cover business studies, computing and vocational skills for employment. Each course pairs classroom teaching with practical projects, so you leave ready for work and further study.</p>
    <p class="body-text">Students also gain access to free online study resources, guided reading lists and career advice sessions.</p>
    <span class="btn">View More Info</span>
  </div>
  <div class="course-teasers">
    <article class="teaser">
      <svg class="teaser-icon" viewBox="0 0 14 14"><rect x="1" y="2" width="12" height="10" fill="none" stroke="#1e9fe0" stroke-width="1.4"/><path d="M1 5h12" stroke="#1e9fe0" stroke-width="1.4"/></svg>
      <div>
        <h3>Business Course</h3>
        <p class="body-text">Management, accounting and marketing classes that prepare you for office roles and career advancement in growing companies.</p>
        <span class="read-more">Read More ›</span>
      </div>
    </article>
    <article class="teaser">
      <svg class="teaser-icon" viewBox="0 0 14 14"><rect x="1" y="2" width="12" height="8" fill="none" stroke="#1e9fe0" stroke-width="1.4"/><path d="M4 13h6M7 10v3" stroke="#1e9fe0" stroke-width="1.4"/></svg>
      <div>
        <h3>Computer Course</h3>
        <p class="body-text">Hands-on computing lessons in office software, networks and programming basics for today's digital workplace.</p>
        <span class="read-more">Read More ›</span>
      </div>
    </article>
  </div>
</section>

<section class="business">
  <div class="business-intro">
    <h2>Business<span>Courses</span></h2>
    <p>Short and full-length programmes for new starters and working professionals.</p>
    <span class="btn ghost">View All Courses ›</span>
  </div>
  <div class="course-card"><div class="photo" role="img" aria-label="Students working together at a laptop"></div><div class="caption"><span>Nemo enim ipsam</span><span>$62,786</span></div></div>
  <div class="course-card"><div class="photo" role="img" aria-label="Smiling student holding folders"></div><div class="caption"><span>Nemo enim ipsam</span><span>$12,786</span></div></div>
  <div class="course-card"><div class="photo" role="img" aria-label="Group of students standing together"></div><div class="caption"><span>Nemo enim ipsam</span><span>$19,786</span></div></div>
</section>

<section class="computer">
  <h2>Computer Courses</h2>
  <p class="subtitle">Build digital skills with practical lessons, expert tutors and free learning resources online.</p>
  <div class="computer-body">
    <div class="monitor" role="img" aria-label="Desktop monitor showing the institute website"></div>
    <div class="features">
      <div class="feature">
        <span class="feature-icon"><svg width="8" height="8" viewBox="0 0 8 8"><circle cx="4" cy="2.5" r="1.8" fill="#1e9fe0"/><path d="M0.5 8a3.5 3 0 0 1 7 0z" fill="#1e9fe0"/></svg></span>
        <div><h3>Expert tutors at every level</h3><p>Learn from qualified trainers with real industry experience.<br>Small classes give everyone attention.</p></div>
      </div>
      <div class="feature">
        <span class="feature-icon"><svg width="8" height="8" viewBox="0 0 8 8"><path d="M1 4l2 2 4-4" fill="none" stroke="#1e9fe0" stroke-width="1.3"/></svg></span>
        <div><h3>Free online study resources</h3><p>Open access to notes, videos and practice tests.<br>Study anywhere, at your own pace.</p></div>
      </div>
      <div class="feature">
        <span class="feature-icon"><svg width="8" height="8" viewBox="0 0 8 8"><rect x="1" y="1.5" width="6" height="5" fill="none" stroke="#1e9fe0" stroke-width="1.2"/></svg></span>
        <div><h3>Career support after training</h3><p>Job guidance, interview practice and placement help.<br>Start your next role with confidence.</p></div>
      </div>
      <span class="btn">View All Courses</span>
    </div>
  </div>
</section>

<footer class="site-footer">
  <div class="contact-row">
    <div><svg width="7" height="9" viewBox="0 0 7 9"><path d="M3.5 9S0 5 0 3.5a3.5 3.5 0 0 1 7 0C7 5 3.5 9 3.5 9z" fill="#9a9a9a"/></svg>12 Harbour Road, Eastfield</div>
    <div><svg width="8" height="8" viewBox="0 0 8 8"><path d="M1 0h2l1 2-1 1a5 5 0 0 0 2 2l1-1 2 1v2a1 1 0 0 1-1 1A7 7 0 0 1 0 1a1 1 0 0 1 1-1z" fill="#9a9a9a"/></svg>Phone: +1 555 0142 880</div>
    <div><svg width="8" height="8" viewBox="0 0 8 8"><rect x="0.5" y="2" width="7" height="5" fill="none" stroke="#9a9a9a"/><rect x="2" y="0.5" width="4" height="2" fill="#9a9a9a"/></svg>Fax: +1 555 0142 881</div>
    <div><svg width="8" height="8" viewBox="0 0 8 8"><circle cx="4" cy="4" r="3.4" fill="none" stroke="#9a9a9a"/><path d="M0.6 4h6.8M4 0.6v6.8" stroke="#9a9a9a" stroke-width=".7"/></svg>www.lanterninstitute.example</div>
  </div>
  <div class="social-row"><span></span><span></span><span></span><span></span><span></span></div>
  <div class="copyright">Copyright © Lantern Institute of Business and Technology. All rights reserved.</div>
</footer>

</div>
</body>
</html>
```